Bright Path Mission- a non profit locin TZ , east Africa. Needing to attract donors.

A flyer for donors /potential partners. showing what their giving has accomplished this year. An Encouraging way to say thank you at the same time informing the partner of the amazing things God is doing with their generous, faithful giving. We will need to print/email. Thank you for considering this project. Your efforts help in educating and feeding 225 street children, providing a safe haven and trade school for hundreds of women and abused teenagers, medical ship on the longest lake in the world going into unreached people groups, a Bible College Training up pastors to plant churches all over TZ, Congo, Burundi and beyond, youth and children’s kids clubs and youth camps. These are the main areas of bright path mission. Bible college, primary school, trade schools, youth camps/kids clubs. We need help in making sure readers will be drawn to seeing/reading more which leads to donations without overwhelming with too much info. HELP! I can tell you about Jesus I have even authored 7 books, but making s flyer that makes sense it out of my wheelhouse. Again, thank you.
Updates

I do not want longer I need quicker and paid for a 3 day quote. All pictures and logo are on our website. I have tried to send pictures but they won’t send. Please look at. Www.brightpathmissiontz.org

Target Market(s)

Professional adults, large companies, donors

Industry/Entity Type

Non profit missionary Bright Path Mission in Tanzania, Congo, USA and soon to be Canada.

Requirements
Must have
• Color professional pictures, feel good, exciting want to be apart of what God is doing
Nice to have
• Glossy trifold
Should not have
• Fly in the face, guilt feeling, animals in Africa

```html
<!DOCTYPE html>
<html lang="en">
<head>
<meta charset="utf-8">
<title>Bright Path Mission – Trifold</title>
<link href="https://fonts.googleapis.com/css2?family=Oswald:wght@500;600&family=Open+Sans:wght@400;700&display=swap" rel="stylesheet">
<style>
  :root{
    --page:#e6e6e6;
    --paper:#ffffff;
    --ink:#3b3b3b;
    --text:#2a2a2a;
    --olive:#9bab5c;
    --olive-light:#cfd8a8;
    --olive-pale:#eef2dc;
    --bar:#474747;
    --photo-warm-1:#8a5a3a;
    --photo-warm-2:#c6422e;
    --photo-warm-3:#d9a441;
    --photo-gray-1:#8c8c8c;
    --photo-gray-2:#d9d9d9;
  }
  *{box-sizing:border-box;margin:0;padding:0}
  html,body{width:900px;height:1200px;overflow:hidden;background:var(--page)}
  .trifold{
    position:absolute;left:30px;top:277px;width:840px;height:646px;
    display:flex;background:var(--paper);
    box-shadow:0 10px 30px rgba(0,0,0,.25);
    font-family:"Open Sans",Arial,sans-serif;color:var(--text);
  }
  .panel{position:relative;height:100%;overflow:hidden}
  .panel--story{width:274px;background:linear-gradient(180deg,var(--olive-pale) 35%,#f7f9ee 60%,var(--olive-light) 92%,var(--olive) 100%)}
  .panel--contact{width:278px;background:var(--paper)}
  .panel--cover{width:288px;background:var(--paper)}

  .photo{position:absolute;left:0;width:100%}
  .photo--celebration{top:0;height:226px;background:linear-gradient(160deg,#6f8f4a 0%,var(--photo-warm-1) 40%,var(--photo-warm-2) 70%,#5b4a36 100%)}
  .photo--celebration::after{content:"";position:absolute;left:0;right:0;bottom:0;height:40px;background:linear-gradient(180deg,rgba(238,242,220,0),var(--olive-pale))}
  .story-text{position:absolute;left:20px;right:18px;top:236px;bottom:10px;overflow:hidden;font-size:8.6px;line-height:11.6px;text-align:justify}
  .story-text p+p{margin-top:11px}

  .photo--gathering{top:0;height:225px;background:linear-gradient(180deg,var(--photo-gray-1) 0%,var(--photo-gray-2) 70%,#fff 100%)}
  .photo--school{top:500px;height:100px;background:linear-gradient(180deg,#fff 0%,var(--photo-gray-2) 35%,#b5b5b5 100%)}
  .bar{position:absolute;left:0;right:0;bottom:0;height:30px;background:var(--bar)}
  .panel--contact .bar{height:46px;background:linear-gradient(180deg,#6a6a6a,var(--bar))}

  .brand{position:absolute;left:0;right:0;display:flex;align-items:center;justify-content:center;gap:8px;
    font-family:"Oswald",Arial Narrow,sans-serif;font-weight:600;color:var(--olive);text-transform:uppercase;letter-spacing:.5px}
  .brand__dot{width:12px;height:12px;border-radius:50%;background:var(--ink)}
  .panel--contact .brand{top:222px;font-size:27px}
  .panel--cover .brand{top:536px;font-size:28px}

  .contact{position:absolute;left:14px;right:14px;text-align:center;font-weight:700;font-size:10.5px;line-height:13.5px;color:var(--text)}
  .contact--address{top:284px}
  .contact--legal{top:336px}
  .contact--phone{top:374px}
  .contact--web{top:388px;font-weight:400;letter-spacing:2px}

  .promise{position:absolute;left:0;right:0;top:426px;text-align:center}
  .promise__title{font-family:"Oswald",Arial Narrow,sans-serif;font-weight:500;font-size:29px;line-height:34px;color:var(--ink);letter-spacing:.5px}
  .promise__line{font-weight:700;font-size:12.5px;color:var(--olive)}

  .cover-head{position:absolute;left:0;right:0;top:14px;text-align:center;font-family:"Oswald",Arial Narrow,sans-serif;text-transform:uppercase}
  .cover-head__lead{font-weight:500;font-size:27px;line-height:32px;color:var(--olive)}
  .cover-head__hope{font-weight:600;font-size:70px;line-height:70px;color:var(--ink);letter-spacing:1px}
  .cover-head__nations{font-weight:500;font-size:34px;line-height:38px;color:var(--olive)}
  .cover-head__sub{margin-top:4px;font-family:"Open Sans",Arial,sans-serif;font-weight:700;font-size:11.5px;line-height:13px;color:var(--text)}
  .photo--children{top:210px;height:298px;background:linear-gradient(120deg,#b98a5c 0%,var(--photo-warm-1) 35%,var(--photo-warm-3) 65%,var(--photo-warm-2) 100%)}
  .cover-web{position:absolute;left:0;right:22px;bottom:0;height:30px;display:flex;align-items:center;justify-content:flex-end;
    color:#fff;font-size:10px;font-weight:700;letter-spacing:2px}
</style>
</head>
<body>
<main class="trifold">

  <section class="panel panel--story">
    <div class="photo photo--celebration" role="img" aria-label="Photo of children in red school uniforms dancing outdoors with a teacher"></div>
    <div class="story-text">
      <p>Bright Path Mission (BPM) has its headquarters in Kigoma, Tanzania, on the longest lake in the world – Lake Tanganyika. It is also the second deepest lake in the world, at close to a mile deep. Over 2 million people live around its shores. Four different countries – Congo, Zambia, Burundi, and Tanzania – have their borders in the lake. Kigoma is a strategic port city. Goods are sent by train from Tanzania's eastern seaport, on the Indian Ocean, to Kigoma's port and loaded on ships to reach the land-locked countries surrounding the lake.</p>
      <p>Daniel and Ruth Ashford founded Bright Path Mission in 2007, but the non-profit has grown much more substantial than just the two of them. Today BPM has six nationals on the missionary staff and employs 45 other locals who help carry on the ministry. Our objective is to raise up nationals who see Jesus as the primary need in this and every nation. Our goal is to make disciples — that's what Jesus told us to do in Matthew 28:19-20. Ultimately that is the only hope any nation has. Our mission is: "To bring hope to the nations through the knowledge of Jesus Christ and the Word of God." (Matt. 12:21)</p>
      <p>How do you bring hope to a nation? There are so many things that can and need to be done in Kigoma, one of the poorest regions in Tanzania. However, we believe it starts with education — and not just a secular education, though that is necessary. The only way to bring hope and affect change in the whole nation is to teach people about Jesus. We approach that goal in many different ways. One is to raise up a new generation that will become godly influencers. There is also a need to educate pastors. Those who are responsible for equipping the Church for the work of the</p>
    </div>
  </section>

  <section class="panel panel--contact">
    <div class="photo photo--gathering" role="img" aria-label="Faded grayscale photo of children holding hands in a circle under a festive tent"></div>
    <div class="brand"><span class="brand__dot"></span>Bright Path Mission</div>
    <p class="contact contact--address">Bright Path Mission<br>PO Box 4820<br>Lodi Springs, CA 95301</p>
    <p class="contact contact--legal">Bright Path Mission is a 501c(3) non-profit<br>corporation. Federal Tax ID # 47-3318205</p>
    <p class="contact contact--phone">get in touch- &nbsp;555 0142 318</p>
    <p class="contact contact--web">brightpathmissiontz.org</p>
    <div class="promise">
      <h2 class="promise__title">IN HIS NAME</h2>
      <p class="promise__line">the nations will put their hope.</p>
    </div>
    <div class="photo photo--school" role="img" aria-label="Grayscale photo of the mission primary school building"></div>
    <div class="bar"></div>
  </section>

  <section class="panel panel--cover">
    <header class="cover-head">
      <p class="cover-head__lead">To Bring</p>
      <h1 class="cover-head__hope">Hope</h1>
      <p class="cover-head__nations">To The Nations</p>
      <p class="cover-head__sub">THROUGH THE KNOWLEDGE OF JESUS<br>CHRIST AND THE WORD OF GOD.</p>
    </header>
    <div class="photo photo--children" role="img" aria-label="Photo of smiling children in colourful beaded clothing"></div>
    <div class="brand"><span class="brand__dot"></span>Bright Path Mission</div>
    <div class="bar"></div>
    <p class="cover-web">brightpathmissiontz.org</p>
  </section>

</main>
</body>
</html>
```